Corporate Design für Voxalento - innovatives Unternehmen im Bereich App-Entwicklung und Kultur
torbelquin perfectly understood the brief and worked with great phantasy. He designed logo, letterhead and cards for our company. Looking forward to working with him again!
Zielgruppe
Gegenstand des Unternehmens ist:
- Entwurf, Entwicklung und Vermarktung von Soziale Netzwerk-Apps für Unternehmen im Kultursektor und für einzelne Kunstprojekte
- Beratung von Kultureinrichtungen
- Technische Umsetzung als Dienstleister von digitalen Apps, Websites, Softwares für den Kulturbereich
- Entwicklung und Erstellung von digitalen Diensten im Kulturbereich
- Entwicklung von Augmented Reality und 3D Technologien für mobile Devices
- Ausbildung im Bereich Kultur und Kreativität
- Erbringung von Dienstleistungen im Media- und Marketingbereich
- Organisation von Kulturveranstaltungen
Zielgruppe sind insbesondere Kreative und Kultureinrichtungen.
www.voxalento.eu
Aufgabenstellung
bitte die Farbe der Website NICHT berücksichtigen. Wir wollen sowieso die Website ändern.
bitte keine Fernseher, Kameras, Videokameras im Logo. Wir bevorzugen etwas abstraktes.
Danke und viel Spass!!

```html
<!DOCTYPE html>
<html lang="de">
<head>
<meta charset="utf-8">
<title>Voxalento – Briefpapier und Visitenkarten</title>
<link href="https://fonts.googleapis.com/css2?family=Jost:wght@300;400;500&display=swap" rel="stylesheet">
<style>
  :root {
    --backdrop: #dcdcdc;
    --paper: #ffffff;
    --ink: #2b2b2b;
    --ink-soft: #444444;
    --card: #494949;
    --card-ink: #ffffff;
    --card-ink-soft: #d8d8d8;
    --brand-blue: #38a9e0;
    --brand-orange: #f8b133;
    --fold-mark: #9a9a9a;
  }
  * { margin: 0; padding: 0; box-sizing: border-box; }
  html, body { width: 1200px; height: 1172px; overflow: hidden; }
  body {
    position: relative;
    background: var(--backdrop);
    font-family: "Jost", sans-serif;
    color: var(--ink);
  }

  /* Letterhead */
  .letterhead {
    position: absolute; left: 62px; top: 69px;
    width: 728px; height: 1031px;
    background: var(--paper);
  }
  .letterhead > * { position: absolute; }
  .brand {
    display: flex; align-items: center; gap: 14px;
  }
  .letterhead .brand { left: 420px; top: 62px; }
  .brand-dot {
    border-radius: 50%;
    background: var(--brand-orange);
    flex: none;
  }
  .letterhead .brand-dot { width: 58px; height: 58px; }
  .brand-name {
    font-weight: 400;
    color: var(--brand-blue);
    letter-spacing: 0.5px;
    line-height: 1;
  }
  .letterhead .brand-name { font-size: 52px; }

  .sender-line { left: 69px; top: 153px; font-size: 9.5px; font-weight: 400; }
  .recipient { left: 69px; top: 205px; font-size: 15px; font-weight: 300; line-height: 17.5px; color: var(--ink); }

  .reference-row { left: 0; top: 330px; width: 728px; height: 30px; font-size: 10.8px; font-weight: 300; line-height: 13.5px; color: var(--ink-soft); }
  .reference-row span { position: absolute; text-align: center; width: 140px; }
  .reference-row .ref-a { left: 101px; }
  .reference-row .ref-b { left: 278px; }
  .reference-row .ref-c { left: 454px; }
  .reference-row .ref-date { right: 41px; width: auto; text-align: right; }

  .fold-mark { left: 0; width: 7px; height: 1px; background: var(--fold-mark); }
  .fold-mark.first { top: 364px; }
  .fold-mark.second { top: 546px; }
  .fold-mark.third { top: 728px; }

  .letter-body { left: 83px; width: 632px; font-size: 10.8px; line-height: 13.3px; font-weight: 400; color: var(--ink); }
  .salutation { top: 401px; }
  .letter-text { top: 468px; }
  .letter-text p { margin-bottom: 13.3px; }
  .closing { top: 693px; }

  .footer-note {
    left: 83px; top: 981px; width: 566px;
    font-size: 6.6px; line-height: 8.9px; text-align: justify;
    text-align-last: justify; font-weight: 400; color: var(--ink);
  }

  /* Business cards */
  .business-card {
    position: absolute; width: 318px; height: 205px;
    background: var(--card); color: var(--card-ink);
  }
  .card-front { left: 831px; top: 249px; }
  .card-back { left: 832px; top: 490px; }
  .card-front .brand { position: absolute; left: 0; right: 0; top: 0; bottom: 0; justify-content: center; gap: 9px; }
  .card-front .brand-dot { width: 30px; height: 30px; }
  .card-front .brand-name { font-size: 30px; color: var(--card-ink); }

  .card-back { text-align: center; }
  .holder-name { position: absolute; left: 0; right: 0; top: 48px; font-size: 19.5px; font-weight: 500; letter-spacing: 0.2px; }
  .holder-role { position: absolute; left: 0; right: 0; top: 74px; font-size: 10px; font-weight: 400; color: var(--card-ink-soft); }
  .contact-list { position: absolute; left: 0; right: 0; top: 101px; font-size: 10px; line-height: 14.6px; list-style: none; }
  .contact-list .label { color: var(--card-ink-soft); margin-right: 6px; }
  .contact-list .value { font-weight: 500; letter-spacing: 0.6px; }
</style>
</head>
<body>

<section class="letterhead" aria-label="Briefbogen">
  <div class="brand">
    <span class="brand-dot"></span>
    <span class="brand-name">Voxalento</span>
  </div>

  <p class="sender-line">Am di voluptation pariam quatiae ma exerior</p>

  <address class="recipient" style="font-style:normal">
    Mustertext<br>
    Hauptstraße 1<br>
    08080 Mustertext
  </address>

  <div class="reference-row">
    <span class="ref-a">Millo que,<br>et mod et aliqui</span>
    <span class="ref-b">Nequae abor<br>andia solupta</span>
    <span class="ref-c">in nonet fugit<br>ratemqui al</span>
    <span class="ref-date">01.01.1900</span>
  </div>

  <span class="fold-mark first"></span>
  <span class="fold-mark second"></span>
  <span class="fold-mark third"></span>

  <p class="letter-body salutation">Lorrovidit quia nobit dit, ut hilit,</p>

  <div class="letter-body letter-text">
    <p>simusandem nimint volut oditatia de re sequi undis aut reprecus si sit rehenia simoditiis dolorerum aut et que inimendam, consedi bernat faccuptatio torum explaut adit reptas dolorent labor accabori voluptatatus de volorenit rerferumque nihit mil ipsaes as as eiciissi vendica estius, idebis erchil explaut a pror aut repedit molutemporem nus maion pero eum as velest odi illaudae od earcien isciet, optaere moluptisit, nimi, omnimporrum de ma culparunt aut que volorempori omnihit, to eossunt mil molupiendae.</p>
    <p>ne enimpor am aut ut ut alis delitas verum non rem sa quiam volor alignam quam, ut que eos intint doluptassit, coremol uptatia sinvenia conseque porro eostiantur rerferitiis est verum sum et doluptam il ium dolorer ovidipi ctatur alia volo modipiendis quat qui re praturendit quunto que volorem olorro tem quam verferspic te qui doloruptae pro cullupta velloreped quodisita nonectatum aceaqui tem et porum id quam ducillaut ventis cupta ditam quatint es ut eatio.</p>
    <p>Di torruptati velecta sperecae perum se num esenis dolore asinulpa cum quaestibus et il min non nos aut velis doluptatet aut arionsequas quost, od quatibus re sit velenis doluptur acepudam, voluptat.</p>
  </div>

  <p class="letter-body closing">Ga. Ut dem nese incia quam iducient.</p>

  <p class="footer-note">Usapiet officilit estibus, ne ea enimeni stiberfernam nonemque doluptatusti dolorib ernates totatus. Beatem fugit optionserum fuga. Nam sam rae volupid elignimet quo. Nus, comnihi liquat excesci tiaspe corrum etum velenih icatur? Sedi odi verchic aborece prem quossit emporpo rrorum as aperunt qui dignate mporit, volenisimus eum lab inis sit archit modi iur seque aperum fugia non eum</p>
</section>

<section class="business-card card-front" aria-label="Visitenkarte Vorderseite">
  <div class="brand">
    <span class="brand-dot"></span>
    <span class="brand-name">Voxalento</span>
  </div>
</section>

<section class="business-card card-back" aria-label="Visitenkarte Rückseite">
  <h1 class="holder-name">Max Mustermann</h1>
  <p class="holder-role">Geschäftsführer</p>
  <ul class="contact-list">
    <li><span class="label">Mobil:</span><span class="value">01234/12345678</span></li>
    <li><span class="label">Fax:</span><span class="value">01234/12345679</span></li>
    <li><span class="label">E-Mail:</span><span class="value" style="letter-spacing:0">m.mustermann@domain.de</span></li>
  </ul>
</section>

</body>
</html>
```